Update New Business Card - For Start Up

I need to update my business card, I have our old version for example. I would like to keep to the same colors and theme. We are a threat reporting and case management tool for corporations and educational institutions.

Target Market(s)

Corporate Security and Human Resources, School Administrators and Superintendents.

Industry/Entity Type

Physical Security and Technology.

Contact Information for Business Card

My Name, Founder/CEO, phone number 555-214-6082, Logo, Web...

Colors
0054AA
0677BA
7BADD7
CADEEF
E8F1F8

Requirements
Must have
• Something new and trendy.

```html
<!DOCTYPE html>
<html lang="en">
<head>
<meta charset="utf-8">
<title>Vigilora Business Card</title>
<link rel="stylesheet" href="https://fonts.googleapis.com/css2?family=Montserrat:wght@600;700&family=Roboto:wght@400&display=swap">
<style>
  :root {
    --stage: #979797;
    --brand: #1e73b9;
    --paper: #ffffff;
    --shadow: rgba(0,0,0,0.55);
  }
  * { margin: 0; padding: 0; box-sizing: border-box; }
  html, body { width: 1075px; height: 1200px; overflow: hidden; background: var(--stage); }
  .stage { position: relative; width: 1075px; height: 1200px; }
  .card {
    position: absolute; width: 664px; height: 395px; overflow: hidden;
    box-shadow: 3px 3px 2px var(--shadow);
  }
  .card--front { left: 206px; top: 187px; background: var(--paper); }
  .card--back { left: 203px; top: 637px; background: var(--brand); }

  .band { position: absolute; left: 0; top: 80px; width: 430px; height: 242px; background: var(--brand); }
  .emblem {
    position: absolute; left: 358px; top: 52px; width: 290px; height: 290px; border-radius: 50%;
    background: var(--brand); border: 7px solid var(--paper); box-shadow: 0 0 0 3px var(--brand);
    display: flex; align-items: center; justify-content: center;
  }
  .emblem__name {
    font-family: 'Montserrat', sans-serif; font-weight: 700; font-size: 30px;
    letter-spacing: 3px; color: var(--paper);
  }
  .identity { position: absolute; left: 38px; top: 118px; color: var(--paper); }
  .identity__name {
    font-family: 'Montserrat', sans-serif; font-weight: 700; font-size: 23px;
    letter-spacing: 1.5px; line-height: 26px;
  }
  .identity__role { font-family: 'Roboto', sans-serif; font-size: 19px; line-height: 22px; }

  .contacts { position: absolute; left: 35px; top: 188px; list-style: none; }
  .contacts__item {
    display: flex; align-items: center; height: 31px;
    font-family: 'Roboto', sans-serif; font-size: 18px; color: var(--paper);
  }
  .contacts__icon { width: 26px; height: 26px; margin-right: 10px; flex: none; }

  .wordmark {
    position: absolute; left: 0; top: 0; width: 100%; height: 100%;
    display: flex; align-items: center; justify-content: center; gap: 14px;
  }
  .wordmark__dot { width: 70px; height: 70px; border-radius: 50%; background: var(--paper); }
  .wordmark__name {
    font-family: 'Montserrat', sans-serif; font-weight: 600; font-size: 34px;
    letter-spacing: 5px; color: var(--paper);
  }
</style>
</head>
<body>
<main class="stage">
  <section class="card card--front">
    <div class="band"></div>
    <div class="emblem"><span class="emblem__name">VIGILORA</span></div>
    <div class="identity">
      <p class="identity__name">DANA WHITFIELD</p>
      <p class="identity__role">Founder / CEO</p>
    </div>
    <ul class="contacts">
      <li class="contacts__item">
        <svg class="contacts__icon" viewBox="0 0 26 26" aria-hidden="true">
          <circle cx="13" cy="13" r="13" fill="#fff"/>
          <path d="M8.5 6.5l2.5-.5 1.3 3.3-1.6 1.2a8 8 0 0 0 4.8 4.8l1.2-1.6 3.3 1.3-.5 2.5c-.3 1-1.3 1.5-2.3 1.3A12 12 0 0 1 7.2 8.8c-.2-1 .3-2 1.3-2.3z" fill="#1e73b9"/>
        </svg>
        555-214-6082
      </li>
      <li class="contacts__item">
        <svg class="contacts__icon" viewBox="0 0 26 26" aria-hidden="true">
          <circle cx="13" cy="13" r="13" fill="#fff"/>
          <rect x="6" y="8.5" width="14" height="9.5" fill="none" stroke="#1e73b9" stroke-width="1.6"/>
          <path d="M6 8.5l7 5.5 7-5.5" fill="none" stroke="#1e73b9" stroke-width="1.6"/>
        </svg>
        dana@vigilora.co
      </li>
      <li class="contacts__item">
        <svg class="contacts__icon" viewBox="0 0 26 26" aria-hidden="true">
          <circle cx="13" cy="13" r="13" fill="#fff"/>
          <g fill="none" stroke="#1e73b9" stroke-width="1.3">
            <circle cx="13" cy="13" r="7"/>
            <ellipse cx="13" cy="13" rx="3" ry="7"/>
            <path d="M6 13h14M7 9.5h12M7 16.5h12"/>
          </g>
        </svg>
        www.vigilora.co
      </li>
    </ul>
  </section>

  <section class="card card--back">
    <div class="wordmark">
      <span class="wordmark__dot"></span>
      <span class="wordmark__name">VIGILORA</span>
    </div>
  </section>
</main>
</body>
</html>
```